Revise my existing consulting brief with new logo

I just got a logo from Pixel Harbor for my new management consulting business, and would like to add it to my existing consulting brief, both 1 and 2 page versions, and would like to improve the layout of these documents to make them look more professional. These documents are essentially the brochure or flyer for my business, so they need to be easy to read and understand quickly. I would like these to be either ppt or Word format so that I can update wording in future, and so that I can save to pdf when I want to share with prospective clients. My new logo print file is attached here, as well as the consulting brief documents that need new layout.
Colors and layout used in the revised consulting brief that you will produce should be aligned to the new logo
Updates

Many of you proposed designs that took into account just one of the 2 documents I sent. However, please be advised that I am looking for designs for both documents that I sent, which are 1- and 2-paged versions of my consulting brief, which is essentially a flyer or brochure that explains my consulting service.

This should not look like a resume, but should be more attractive as a kind of business flyer/brochure.

Please also be aware that I am open to landscape format designs, not just portrait, which would be more in line with the versions I sent you.

Target Market(s)

Pharmaceutical and medical device companies

Industry/Entity Type

Pharmaceutical and medical device

Font styles to use
Serif
Sans Serif

Requirements
Must have
• Color and look that align to my new logo. Ability for me to update the text later on my own as needed, so that I can adapt it to different clients.
Should not have
• I am not looking for a PowerPoint template or stationary to match my logo. I am just looking to have the consulting briefs that I sent revised so that they fit the new logo and look more professional in layout.

```html
<!DOCTYPE html>
<html lang="en">
<head>
<meta charset="utf-8">
<title>Clearpath Consulting – Consulting Brief</title>
<link href="https://fonts.googleapis.com/css2?family=Montserrat:wght@400;500;600;700;800&display=swap" rel="stylesheet">
<style>
:root{
  --navy:#22408f;
  --navy-deep:#1b2f6e;
  --teal:#17b8c0;
  --teal-light:#5fd0d6;
  --ink:#3c3f48;
  --paper:#ffffff;
  --panel:#f3f4f7;
  --rule:#b9c3db;
  --stage:#e6e8ed;
}
*{box-sizing:border-box;margin:0;padding:0}
html,body{width:1122px;height:1200px;overflow:hidden}
body{background:var(--stage);font-family:"Montserrat",sans-serif;color:var(--ink);position:relative}
.page{position:absolute;top:214px;width:545px;height:772px;background:var(--paper);overflow:hidden;box-shadow:0 4px 14px rgba(20,30,60,.18)}
.page--one{left:10px}
.page--two{left:567px}
.abs{position:absolute}
svg.abs{display:block}

/* contacts */
.contacts{position:absolute;right:16px;top:24px;text-align:right;color:#fff;font-size:10.5px;line-height:21px;font-weight:500}
.contacts li{list-style:none;display:flex;justify-content:flex-end;align-items:center;gap:9px}
.contacts .phone-line{font-size:12.5px}
.contacts--dark{color:var(--navy)}
.ico{width:14px;height:14px;border-radius:50%;background:var(--teal);display:inline-flex;align-items:center;justify-content:center;flex:none}
.ico svg{width:9px;height:9px}

/* page one */
.brand{position:absolute;left:18px;top:36px;width:190px}
.brand-name{font-size:27px;font-weight:800;color:var(--navy);line-height:1;letter-spacing:-.5px}
.brand-sub{font-size:12.5px;font-weight:800;color:var(--navy);letter-spacing:3.2px;margin-top:4px}
.brand-mark{display:inline-block;width:12px;height:12px;background:var(--teal);border-radius:50%;margin-right:6px;vertical-align:3px}
.hero-photo{position:absolute;left:0;top:111px;width:545px;height:247px;background:linear-gradient(100deg,#1c2e66 0%,#2b4a8e 45%,#3d8fb6 75%,#2a5f96 100%)}
.hero-title{position:absolute;left:17px;top:128px;color:#fff;font-size:24.5px;font-weight:700;line-height:28px;letter-spacing:-.2px}
.hero-rule{position:absolute;left:17px;top:225px;width:300px;height:2px;background:var(--teal)}
.hero-tag{position:absolute;left:17px;top:232px;color:#fff;font-size:14px;font-weight:500;line-height:18px}
.bio{position:absolute;left:17px;top:293px;width:480px;color:#fff;font-size:8.6px;line-height:12.8px}
.bio-name{font-size:12px;font-weight:800;letter-spacing:.2px;margin-bottom:1px}
.bio-name span{color:var(--teal)}
.section-tab{position:absolute;left:0;top:372px;height:22px}
.section-tab-label{position:absolute;left:17px;top:377px;color:#fff;font-size:10px;font-weight:700;letter-spacing:.2px}
.cap-row{position:absolute;left:0;width:545px}
.cap-name{position:absolute;left:0;top:0;bottom:0;width:161px;background:var(--panel);padding:18px 10px 0 16px;color:var(--navy);font-size:12.5px;font-weight:700;line-height:12.8px}
.cap-detail{position:absolute;left:166px;right:0;top:0;bottom:0;background:var(--panel);padding:17px 14px 0 4px}
.cap-row + .cap-row .cap-name,.cap-row + .cap-row .cap-detail{border-top:1px solid var(--rule)}
.bullets{list-style:none;font-size:9.1px;line-height:12.8px}
.bullets li{position:relative;padding-left:14px}
.bullets li::before{content:"";position:absolute;left:1px;top:3px;width:5px;height:5px;border-right:1.6px solid var(--navy);border-top:1.6px solid var(--navy);transform:rotate(45deg)}
.footer-band{position:absolute;left:0;bottom:0;width:545px;height:30px}

/* page two */
.portrait-frame{position:absolute;left:27px;top:27px;width:207px;height:204px;background:linear-gradient(135deg,#8f94cc,#cfd2ee)}
.portrait{position:absolute;left:35px;top:34px;width:192px;height:192px;background:radial-gradient(circle at 50% 42%,#b0765e 0%,#8a5a48 30%,#6e6f78 62%,#8b8d96 100%)}
.about-tab{position:absolute;left:233px;top:122px}
.about-title{position:absolute;left:243px;top:124px;color:#fff;font-size:14.5px;font-weight:700}
.about-lead{position:absolute;left:242px;top:150px;width:285px;font-size:9.1px;line-height:12.9px}
.about-line{position:absolute;font-size:9.1px;line-height:12.9px;white-space:nowrap}
.banner{position:absolute;left:0;top:394px;width:545px;height:57px;background:linear-gradient(90deg,var(--teal) 0%,#23b9c6 60%,#1fbec4 100%);padding:10px 17px 0;color:#fff;font-size:12.6px;font-weight:700;line-height:15.6px}
.achievements{position:absolute;left:17px;top:463px;width:510px;list-style:none;font-size:9.1px;line-height:12.9px}
.achievements li{position:relative;padding-left:17px;margin-bottom:12.3px}
.achievements li::before{content:"";position:absolute;left:1px;top:3px;width:5px;height:5px;border-right:1.6px solid var(--navy);border-top:1.6px solid var(--navy);transform:rotate(45deg)}
.achievements strong{color:var(--navy);font-weight:700}
</style>
</head>
<body>

<!-- PAGE ONE -->
<section class="page page--one" aria-label="Consulting brief page one">
  <svg class="abs" style="left:0;top:0" width="545" height="111" viewBox="0 0 545 111">
    <rect width="545" height="111" fill="var(--panel)"/>
    <polygon points="196,0 545,0 545,111 306,111" fill="var(--navy)"/>
  </svg>
  <div class="brand">
    <div class="brand-name"><span class="brand-mark"></span>CLEARPATH</div>
    <div class="brand-sub">ADVISORY LLC</div>
  </div>
  <ul class="contacts">
    <li class="phone-line">555 014 2287 <span class="ico"><svg viewBox="0 0 10 10"><path d="M2 1l2 2-1 1c.6 1.3 1.6 2.3 3 3l1-1 2 2-1.4 1.3C4.5 9 1 5.5.7 2.4z" fill="#fff"/></svg></span></li>
    <li>helena.marchetti@example.com <span class="ico"><svg viewBox="0 0 10 10"><rect x="1" y="2.5" width="8" height="5.5" fill="none" stroke="#fff" stroke-width="1"/><path d="M1 2.5l4 3 4-3" fill="none" stroke="#fff" stroke-width="1"/></svg></span></li>
    <li>www.example.com/in/helena-marchetti <span class="ico"></span></li>
  </ul>

  <div class="hero-photo" role="img" aria-label="Photo of business team reviewing charts and documents at a desk"></div>
  <svg class="abs" style="left:0;top:111px" width="545" height="247" viewBox="0 0 545 247">
    <defs>
      <linearGradient id="shade1" x1="0" x2="1" y1="0" y2="0">
        <stop offset="0" stop-color="#1b2e64" stop-opacity=".92"/>
        <stop offset=".6" stop-color="#22408f" stop-opacity=".55"/>
        <stop offset="1" stop-color="#22408f" stop-opacity="0"/>
      </linearGradient>
      <linearGradient id="tealTri" x1="0" x2="1" y1="0" y2="1">
        <stop offset="0" stop-color="#5fd0d6" stop-opacity=".2"/>
        <stop offset="1" stop-color="#17b8c0"/>
      </linearGradient>
    </defs>
    <rect width="545" height="247" fill="url(#shade1)"/>
    <polygon points="300,0 545,0 545,247" fill="url(#tealTri)" opacity=".85"/>
    <rect y="171" width="545" height="76" fill="#141d3d" opacity=".82"/>
    <polygon points="470,171 545,171 545,247" fill="var(--teal)" opacity=".9"/>
  </svg>
  <h1 class="hero-title">Clearpath Consulting<br>Helena Marchetti,<br>Independent Consultant</h1>
  <div class="hero-rule"></div>
  <p class="hero-tag">Solving Complex Challenges<br>Driving Programs From Strategy To Action</p>
  <div class="bio">
    <div class="bio-name">HELENA <span>MARCHETTI</span></div>
    helps companies tackle and succeed in making change by providing project leadership and program management services for key business objectives. She understands the importance of getting it right the first time, and specializes in shaping solutions to drive complex business initiatives from strategy to action.
  </div>

  <svg class="section-tab" width="230" height="22" viewBox="0 0 230 22">
    <defs><linearGradient id="tab1" x1="0" x2="1"><stop offset="0" stop-color="var(--navy)"/><stop offset=".65" stop-color="var(--navy)"/><stop offset="1" stop-color="var(--teal)"/></linearGradient></defs>
    <polygon points="0,0 208,0 228,22 0,22" fill="url(#tab1)"/>
  </svg>
  <div class="section-tab-label">EXPERTISE AND CAPABILITIES:</div>

  <div class="cap-row" style="top:409px;height:94px">
    <div class="cap-name">Mergers and<br>Acquisitions</div>
    <div class="cap-detail"><ul class="bullets">
      <li>For companies acquiring a target: Build integration teams, lead team in developing integration plan &amp; budget, facilitate planning for an efficient and effective Day 1, and for 30-60-90 day horizon</li>
      <li>Assist companies looking to be acquired to prepare their people, processes and systems for due diligence</li>
    </ul></div>
  </div>
  <div class="cap-row" style="top:503px;height:115px">
    <div class="cap-name">Inflation<br>Reduction Act</div>
    <div class="cap-detail"><ul class="bullets">
      <li>Drug price negotiation operational readiness: Put in place process and governance for submission development and ensuring engagements with CMS. Identify cross-functional team members needed, design approval processes, build and oversee integrated project plan and timeline.</li>
      <li>Part D redesign readiness: Identify gaps and develop plan to address, including chartering workstreams and creation and implementation of plans and timelines to drive from strategy to execution</li>
    </ul></div>
  </div>
  <div class="cap-row" style="top:618px;height:124px">
    <div class="cap-name">Strategic Programs<br>&amp; Business<br>Transformation</div>
    <div class="cap-detail"><ul class="bullets">
      <li>Develop strategy, framework and governance to accomplish organization and business model change, inclusive of people, processes and systems</li>
      <li>Change Management for new ways of working and new business models</li>
      <li>Facilitate goal-setting and strategic prioritization exercises with leadership teams</li>
    </ul></div>
  </div>

  <svg class="footer-band" viewBox="0 0 545 30" preserveAspectRatio="none">
    <defs><linearGradient id="foot1" x1="0" x2="1"><stop offset="0" stop-color="var(--navy)"/><stop offset=".55" stop-color="#2e5aa0"/><stop offset="1" stop-color="var(--teal)"/></linearGradient></defs>
    <rect width="545" height="30" fill="url(#foot1)"/>
    <path d="M215 30 Q260 2 340 0 L300 0 Q245 4 200 30Z" fill="#6cc6dc" opacity=".6"/>
    <path d="M400 30 Q440 2 545 0 L545 8 Q470 10 430 30Z" fill="#a8e3ea" opacity=".55"/>
  </svg>
</section>

<!-- PAGE TWO -->
<section class="page page--two" aria-label="Consulting brief page two">
  <svg class="abs" style="left:0;top:0" width="545" height="394" viewBox="0 0 545 394">
    <rect width="545" height="394" fill="var(--panel)"/>
    <polygon points="0,0 350,0 0,350" fill="var(--navy)"/>
  </svg>
  <div class="portrait-frame"></div>
  <div class="portrait" role="img" aria-label="Headshot portrait of the consultant"></div>
  <ul class="contacts contacts--dark">
    <li class="phone-line">555 014 2287 <span class="ico"><svg viewBox="0 0 10 10"><path d="M2 1l2 2-1 1c.6 1.3 1.6 2.3 3 3l1-1 2 2-1.4 1.3C4.5 9 1 5.5.7 2.4z" fill="#fff"/></svg></span></li>
    <li>helena.marchetti@example.com <span class="ico"><svg viewBox="0 0 10 10"><rect x="1" y="2.5" width="8" height="5.5" fill="none" stroke="#fff" stroke-width="1"/><path d="M1 2.5l4 3 4-3" fill="none" stroke="#fff" stroke-width="1"/></svg></span></li>
    <li>www.example.com/in/helena-marchetti <span class="ico"></span></li>
  </ul>

  <svg class="about-tab" width="238" height="23" viewBox="0 0 238 23">
    <defs><linearGradient id="tab2" x1="0" x2="1"><stop offset="0" stop-color="var(--navy)"/><stop offset=".6" stop-color="var(--navy)"/><stop offset="1" stop-color="var(--teal)"/></linearGradient></defs>
    <polygon points="0,0 215,0 237,23 0,23" fill="url(#tab2)"/>
  </svg>
  <h2 class="about-title">About Helena Marchetti:</h2>
  <p class="about-lead">As a passionate executive with 25 years of Pharmaceutical and MedTech expertise at Meridian Health Group, Helena is now helping companies achieve business results by providing leadership and oversight for key objectives and initiatives. She brings clarity to the complex and pioneers the way forward to solve new problems, leading critical business programs to rapid and seamless execution.</p>

  <div class="about-para about-para--known">
    <p class="about-line" style="left:100px;top:257px">Ms. Marchetti is known for uncovering new solutions, connecting the dots, building strong</p>
    <p class="about-line" style="left:88px;top:270px">cross-functional relationships, and driving engagement across teams.</p>
  </div>
  <div class="about-para about-para--marketing">
    <p class="about-line" style="left:63px;top:296px">Helena leverages her robust marketing background to enhance strategic transformations by infusing</p>
    <p class="about-line" style="left:51px;top:309px">customer-centric insights, effective communication, and commercial focus. Her marketing roles included</p>
    <p class="about-line" style="left:38px;top:322px">product development and launch, global portfolio management, managing alliances for innovative external</p>
    <p class="about-line" style="left:26px;top:335px">partnerships and KOL development.</p>
  </div>
  <div class="about-para about-para--citizen">
    <p class="about-line" style="left:17px;top:360px">Ms. Marchetti is a dual citizen of France and the US, and has lived and worked on two continents. She leverages</p>
    <p class="about-line" style="left:17px;top:373px">her cross-cultural know-how to advance business collaboration and business goals.</p>
  </div>

  <div class="banner">Helena has held leadership roles in Marketing, M&amp;A, Business Transformation and Strategy &amp; Operations. Her achievements include:</div>

  <ul class="achievements">
    <li><strong>Directed enterprise-wide integration team</strong> accountable for integrating a foot &amp; ankle implants company into Meridian: transitioned from distributors to direct sales force, doubled production, met quality remediation goals, orchestrated organizational structure &amp; technology changes, and moved customer service and distribution.</li>
    <li><strong>Led integration</strong> and new business model implementation of a critical asset in the Joint Reconstruction space that resulted in increased product pull-through, exceeding deal model expectations by double digits.</li>
    <li><strong>Drove business readiness</strong> and company response to the unprecedented changes stemming from the Inflation Reduction Act. Led operations for 2 drug price negotiation submissions to CMS. Created and facilitated program of 6 workstreams, leading IRA transformation activities.</li>
    <li><strong>Strategy &amp; Ops lead for launch</strong> of company's first CAR-T cell therapy. Dove in deep with a series of workshops to define launch plan and interdependencies, designed and implemented team structure and project governance, navigated changing landscape and unforeseen challenges, resulting in a best-in-class launch that has become a role model in the cell and gene therapy space.</li>
    <li><strong>As Strategic Business Transformation</strong> lead for US Oncology business, orchestrated strategy and operations excellence, including business goal-setting, strategic planning process, leadership business reviews and oversight of launch planning for 5 new drugs.</li>
  </ul>

  <svg class="footer-band" viewBox="0 0 545 30" preserveAspectRatio="none">
    <defs><linearGradient id="foot2" x1="0" x2="1"><stop offset="0" stop-color="var(--navy)"/><stop offset=".55" stop-color="#2e5aa0"/><stop offset="1" stop-color="var(--teal)"/></linearGradient></defs>
    <rect width="545" height="30" fill="url(#foot2)"/>
    <path d="M215 30 Q260 2 340 0 L300 0 Q245 4 200 30Z" fill="#6cc6dc" opacity=".6"/>
    <path d="M400 30 Q440 2 545 0 L545 8 Q470 10 430 30Z" fill="#a8e3ea" opacity=".55"/>
  </svg>
</section>

</body>
</html>
```